Corporate Business Card

Very professional, Modern, Not to busy, include phone address email, website
(253) 555-0174, 61807 19th Street N, Kent, WA 98517, marcus@kestrelbayholding.com, brelvanindustries.com

Target Market(s)

Manufacturing

Industry/Entity Type

Aero, machining, manufacturing, Off road racing

Contact Information for Business Card

Phone, address email, website

```html
<!DOCTYPE html>
<html lang="en">
<head>
<meta charset="utf-8">
<title>Brelvan Industries — Business Card</title>
<link href="https://fonts.googleapis.com/css2?family=Carlito:wght@400;700&display=swap" rel="stylesheet">
<style>
  :root {
    --backdrop: #ababab;
    --navy: #1b3a73;
    --navy-deep: #16326a;
    --pattern-light: #2a4a85;
    --card-white: #ffffff;
    --ink: #222222;
    --ink-soft: #555555;
  }
  * { box-sizing: border-box; margin: 0; padding: 0; }
  html, body {
    width: 1200px; height: 1000px; overflow: hidden;
    background: var(--backdrop);
    font-family: "Carlito", "Calibri", sans-serif;
  }
  .canvas { position: relative; width: 1200px; height: 1000px; }

  .card {
    position: absolute; top: 196px;
    width: 351px; height: 612px;
    border-radius: 28px; overflow: hidden;
  }

  /* Back of card */
  .card-back { left: 206px; background: var(--navy); }
  .card-back .brand-pattern {
    position: absolute; inset: 0;
    background: linear-gradient(180deg, var(--pattern-light) 0%, var(--navy) 45%, var(--navy-deep) 100%);
  }
  .card-back .brand-mark {
    position: absolute; left: 127px; top: 532px; width: 100px;
    text-align: center; color: var(--card-white);
    font-weight: 700; line-height: 1;
  }
  .card-back .brand-mark .name { font-size: 22px; letter-spacing: 0.5px; display: block; }
  .card-back .brand-mark .sub { font-size: 9px; display: block; margin-top: 2px; }

  /* Front of card */
  .card-front { left: 612px; background: var(--card-white); text-align: center; }
  .card-front .brand-name {
    position: absolute; top: 192px; left: 0; right: 0;
    color: var(--navy); font-weight: 700; line-height: 1;
  }
  .card-front .brand-name .name { display: block; font-size: 50px; letter-spacing: 1px; }
  .card-front .brand-name .sub { display: block; font-size: 20px; margin-top: 4px; }

  .contact-icons {
    position: absolute; top: 336px; left: 0; right: 0;
    display: flex; justify-content: center; gap: 8px;
  }
  .contact-icons svg { width: 19px; height: 19px; }

  .contact-lines {
    position: absolute; top: 368px; left: 0; right: 0;
    color: var(--ink); font-size: 17.5px; line-height: 21.5px;
  }

  .divider {
    position: absolute; top: 452px; left: 76px;
    width: 198px; height: 1.5px; background: var(--navy);
  }

  .address-icon { position: absolute; top: 467px; left: 167px; width: 17px; height: 20px; }

  .address-lines {
    position: absolute; top: 497px; left: 0; right: 0;
    color: var(--ink-soft); font-size: 17.5px; line-height: 22px;
  }
</style>
</head>
<body>
<main class="canvas">

  <section class="card card-back">
    <div class="brand-pattern" role="img" aria-label="Repeating tone-on-tone brand name pattern on navy"></div>
    <div class="brand-mark">
      <span class="name">BRELVAN</span>
      <span class="sub">Industries</span>
    </div>
  </section>

  <section class="card card-front">
    <div class="brand-name">
      <span class="name">BRELVAN</span>
      <span class="sub">Industries</span>
    </div>

    <div class="contact-icons" aria-hidden="true">
      <svg viewBox="0 0 20 20" fill="none" stroke="#1b3a73" stroke-width="1.3" stroke-linejoin="round">
        <path d="M4 2.5l3 .2 1.2 3.4-1.8 1.4c.9 2 2.4 3.6 4.3 4.5l1.4-1.8 3.4 1.2.2 3c-.1.8-.8 1.3-1.6 1.3C8.3 15.5 3.6 10.8 2.7 4.1c0-.8.5-1.5 1.3-1.6z"/>
        <path d="M12 2.5a5.5 5.5 0 0 1 5 5M11.5 5a3 3 0 0 1 3 3"/>
      </svg>
      <svg viewBox="0 0 20 20" fill="none" stroke="#1b3a73" stroke-width="1.3">
        <rect x="1.5" y="4" width="17" height="12"/>
        <path d="M1.5 4l8.5 7 8.5-7M1.5 16l6-6M18.5 16l-6-6"/>
      </svg>
      <svg viewBox="0 0 20 20" fill="none" stroke="#1b3a73" stroke-width="1.3">
        <circle cx="10" cy="10" r="8"/>
        <ellipse cx="10" cy="10" rx="3.5" ry="8"/>
        <path d="M2 10h16M3.2 6h13.6M3.2 14h13.6"/>
      </svg>
    </div>

    <div class="contact-lines">
      <p>(253) 555-0174</p>
      <p>marcus@kestrelbayholding.com</p>
      <p>brelvanindustries.com</p>
    </div>

    <div class="divider"></div>

    <svg class="address-icon" viewBox="0 0 17 20" fill="none" stroke="#1b3a73" stroke-width="1.4" aria-hidden="true">
      <path d="M8.5 19s6-6.2 6-10.5a6 6 0 0 0-12 0C2.5 12.8 8.5 19 8.5 19z"/>
      <circle cx="8.5" cy="8.5" r="2"/>
    </svg>

    <div class="address-lines">
      <p>61807 19th Street N</p>
      <p>Kent, WA 98517</p>
    </div>
  </section>

</main>
</body>
</html>
```